Non Profit raising scholarship funds needs flyer for Golf Tournament

We need a flyer for our upcoming golf tournament. Proceeds to will help to benefit our Halvern builders learning scholarship fund.

Title: 2019 O-VarTD Golf Tournament
Location: Brackenfield Links
Date: May 15, 2019
Registration: $175 individual, $700 foursome
Sponsorships starting at $250
Benefiting O-VarTD and the Halvern Builders Learning Scholarship Fund

Target Market(s)

Design and Construction industry professionals

Industry/Entity Type

Construction

Font styles to use
Serif
Sans Serif

Colors

Designer to choose colors to be used in the design.

Requirements
Must have
• Title, date, location, registration info, sponsor info, benefit info, logo
Nice to have
• I like the retro look of some golf flyers, but it's not necessary
Should not have
• .

```html
<!DOCTYPE html>
<html lang="en">
<head>
<meta charset="utf-8">
<title>2019 O-VarTD Golf Tournament</title>
<link rel="stylesheet" href="https://fonts.googleapis.com/css2?family=Abril+Fatface&family=Anton&family=Oswald:wght@500;600&family=Playfair+Display:wght@900&display=swap">
<style>
  :root {
    --night: #03050a;
    --deep-blue: #0b2a66;
    --glow-blue: #1d5fc4;
    --fairway-dark: #14260f;
    --fairway: #2d5420;
    --golf-green: #8db33a;
    --lime: #c8e14a;
    --white: #ffffff;
    --ghost: #3a3d44;
    --ball-light: #ffffff;
    --ball-shade: #c9cbce;
  }
  * { margin: 0; padding: 0; box-sizing: border-box; }
  html, body { width: 857px; height: 1200px; overflow: hidden; background: var(--night); }
  .flyer {
    position: relative; width: 857px; height: 1200px; overflow: hidden;
    background:
      radial-gradient(ellipse 380px 320px at 560px 370px, rgba(29,95,196,.75), transparent 70%),
      linear-gradient(135deg, var(--night) 0%, var(--night) 30%, var(--deep-blue) 55%, var(--night) 80%);
  }
  .light-beams { position: absolute; inset: 0; }
  .course-photo {
    position: absolute; left: 0; top: 560px; width: 857px; height: 640px;
    background: linear-gradient(180deg, rgba(3,5,10,0) 0%, var(--fairway-dark) 18%, var(--fairway) 60%, #3b6a2a 100%);
  }
  .eyebrow {
    position: absolute; top: 18px; left: 0; width: 100%; text-align: center;
    font: 500 16px/1 "Oswald", sans-serif; letter-spacing: 30px; color: var(--ghost);
    padding-left: 30px;
  }
  .club-head { position: absolute; width: 123px; height: 92px; background: var(--golf-green); border-radius: 46px 12px 46px 12px; }
  .club-left { left: 0; }
  .club-right { right: 0; }
  .title-year {
    position: absolute; top: 160px; left: 290px; width: 180px; text-align: center;
    font: 400 84px/1 "Anton", sans-serif; color: var(--white);
  }
  .title-golf {
    position: absolute; top: 232px; left: 0; width: 832px; text-align: center;
    font: 400 148px/1 "Abril Fatface", serif; color: var(--golf-green); letter-spacing: 6px;
  }
  .golf-ball {
    position: absolute; left: 291px; top: 207px; width: 176px; height: 176px; border-radius: 50%;
    background: radial-gradient(circle at 40% 35%, var(--ball-light) 40%, var(--ball-shade) 100%);
    display: flex; align-items: center; justify-content: center;
  }
  .ball-name { font: 600 26px/1 "Oswald", sans-serif; color: var(--deep-blue); }
  .title-tournament {
    position: absolute; top: 366px; left: 0; width: 834px; text-align: center;
    font: 400 50px/1.1 "Anton", sans-serif; color: var(--white);
  }
  .details {
    position: absolute; left: 0; width: 857px; text-align: center; white-space: nowrap;
    font: 500 30px/1 "Oswald", sans-serif; color: var(--white);
  }
  .details .label { color: var(--lime); font-weight: 600; }
  .rule { position: absolute; height: 1px; background: var(--lime); opacity: .8; }
  .sponsor-lead {
    position: absolute; top: 1018px; left: 178px; width: 500px; text-align: center; white-space: nowrap;
    font: 900 16px/1 "Playfair Display", serif; color: var(--white); text-transform: uppercase;
  }
  .sponsor-amount {
    position: absolute; top: 1038px; left: 278px; width: 300px; text-align: center; white-space: nowrap;
    font: 400 74px/1 "Abril Fatface", serif; color: var(--golf-green);
  }
  .benefit {
    position: absolute; top: 1120px; left: 178px; width: 500px; text-align: center;
    font: 900 16px/1.6 "Playfair Display", serif; color: var(--white);
  }
</style>
</head>
<body>
<main class="flyer">
  <svg class="light-beams" width="857" height="1200" aria-hidden="true">
    <polygon points="500,40 857,400 857,520 430,90" fill="#0e2f72" opacity=".45"/>
    <polygon points="600,120 857,380 857,430 580,140" fill="#1a4fa8" opacity=".35"/>
    <polygon points="640,250 857,470 857,500 630,260" fill="#000" opacity=".4"/>
  </svg>

  <div class="course-photo" role="img" aria-label="Photo of a golf course fairway at dusk with a red golf bag and clubs standing on the grass"></div>

  <div class="eyebrow">TOURNAMENT</div>

  <div class="club-head club-left" style="top:163px" role="img" aria-label="Green golf club head illustration"></div>
  <div class="club-head club-left" style="top:271px" role="img" aria-label="Green golf club head illustration"></div>
  <div class="club-head club-left" style="top:379px" role="img" aria-label="Green golf club head illustration"></div>
  <div class="club-head club-right" style="top:163px" role="img" aria-label="Green golf club head illustration"></div>
  <div class="club-head club-right" style="top:271px" role="img" aria-label="Green golf club head illustration"></div>
  <div class="club-head club-right" style="top:379px" role="img" aria-label="Green golf club head illustration"></div>

  <h1>
    <span class="title-year">2019</span>
    <span class="title-golf">GOLF</span>
    <span class="title-tournament">Tournament</span>
  </h1>
  <div class="golf-ball" role="img" aria-label="Golf ball carrying the O-VarTD name"><span class="ball-name">O-VarTD</span></div>

  <p class="details" style="top:648px"><span class="label">Location:</span> Brackenfield Links</p>
  <div class="rule" style="left:366px; top:692px; width:288px"></div>
  <p class="details" style="top:708px"><span class="label">Date:</span> May 15, 2019</p>
  <div class="rule" style="left:229px; top:751px; width:257px"></div>
  <p class="details" style="top:768px"><span class="label">Registration:</span> $175 individual, $700 foursome</p>
  <div class="rule" style="left:126px; top:816px; width:605px"></div>

  <p class="sponsor-lead">Sponsorships starting at</p>
  <p class="sponsor-amount">$250</p>
  <p class="benefit">Benefiting O-VarTD and the Halvern Builders<br>Learning Scholarship Fund</p>
</main>
</body>
</html>
```